Brandlark CEO needs a Crowdsourced Graphic for a Gizmoreel Article

I need a simple graphic / banner for a blog post that's going to be posted on Gizmoreel (www.gizmoreel.example) - the biggest tech blog in the world.

The article will be written by Omar Feltz (Brandlark's CEO) and the title will be "The Quiet Harbor Surge Unveiled". The article is about the tens of thousands of people using crowdsourcing websites (like Brandlark.example, Qtaskly.example and Wervo.example) in China, India, the Philippines, Australia and other countries in the Asia Pacific region.

We'd really like to get this ASAP - so early submissions encouraged. We will try and get the winning designer linked to from the article.
Updates

Thanks to everyone that submitted!  Some great designs and hard to choose! :)

Target Market(s)

Tech saavy readers, English speakers

Industry/Entity Type

Tech

Requirements
Must have
• The graphic SHOULD:
1) Have the text "The quiet harbor surge unveiled" with some nice design and fonts (consider grey subtle pattern background and white drop shadow on fonts) - see attached examples
2) Have an Asian theme
3) Have the dimensions 640px wide by 240px wide
Nice to have
• The graphic COULD:
1) Have references to some or all of the countries mentioned above or use Asian characters as part of the background / motif (maybe the word "crowd" or "crowd sourcing" in different languages). In Chinese, the word for crowdsourcing is "witkey" (and there are corresponding Chinese characters: ??)
2) Emphasize the word "Asia" (using color and larger/different font)
3) Use a chart showing exponential (i.e. fast) growth - like the attached
4) Have a second line of text "7 Odd Facts Hiding Behind the Quiet Harbor Surge"

```html
<!DOCTYPE html>
<html lang="en">
<head>
<meta charset="utf-8">
<title>The Quiet Harbor Surge Unveiled</title>
<link rel="stylesheet" href="https://fonts.googleapis.com/css2?family=Bebas+Neue&display=swap">
<style>
  :root {
    --page-bg: #f2f2f2;
    --banner-bg: #ffffff;
    --banner-border: #c9c9c9;
    --pattern-tone: #f3f3f3;
    --chart-tone: #e4e4e4;
    --accent-red: #f0143c;
    --ink-dark: #3a3a3a;
    --white: #ffffff;
  }
  html, body {
    margin: 0;
    width: 1200px;
    height: 900px;
    overflow: hidden;
    background: radial-gradient(circle at 50% 45%, #ffffff 0%, var(--page-bg) 70%, #e6e6e6 100%);
  }
  .stage {
    position: relative;
    width: 1200px;
    height: 900px;
  }
  .banner {
    position: absolute;
    left: 279px;
    top: 329px;
    width: 640px;
    height: 240px;
    background: var(--banner-bg);
    border: 1px solid var(--banner-border);
    overflow: hidden;
    font-family: "Bebas Neue", "Arial Narrow", sans-serif;
  }
  .banner-texture {
    position: absolute;
    inset: 0;
    background: linear-gradient(180deg, var(--pattern-tone) 0%, #fafafa 55%, var(--pattern-tone) 100%);
  }
  .growth-chart {
    position: absolute;
    inset: 0;
  }
  .headline {
    position: absolute;
    left: 26px;
    top: 8px;
    margin: 0;
    font-weight: 400;
    text-shadow: 1px 1px 0 var(--white);
  }
  .headline-emphasis {
    display: block;
    color: var(--accent-red);
    font-size: 122px;
    line-height: 0.92;
    letter-spacing: 0.5px;
  }
  .headline-rest {
    display: block;
    color: var(--ink-dark);
    font-size: 49px;
    line-height: 1;
    margin-top: -2px;
  }
  .subline {
    position: absolute;
    left: 24px;
    top: 194px;
    display: flex;
    align-items: center;
    gap: 9px;
    margin: 0;
    color: var(--ink-dark);
    font-size: 28px;
    line-height: 1;
    text-shadow: 1px 1px 0 var(--white);
  }
  .subline-number {
    display: inline-flex;
    align-items: center;
    justify-content: center;
    width: 32px;
    height: 32px;
    border-radius: 50%;
    background: var(--accent-red);
    color: var(--white);
    font-size: 24px;
    text-shadow: none;
    padding-top: 2px;
    box-sizing: border-box;
  }
</style>
</head>
<body>
  <main class="stage">
    <section class="banner" aria-label="Article header graphic">
      <div class="banner-texture" role="img" aria-label="Subtle grey lattice pattern background"></div>
      <svg class="growth-chart" viewBox="0 0 640 240" aria-hidden="true">
        <polyline points="230,250 318,172 420,162 500,88 580,54 660,-10"
                  fill="none" stroke="var(--chart-tone)" stroke-width="4" stroke-linejoin="round"/>
        <circle cx="318" cy="172" r="17" fill="var(--chart-tone)"/>
        <circle cx="420" cy="162" r="17" fill="var(--chart-tone)"/>
        <circle cx="500" cy="88" r="17" fill="var(--chart-tone)"/>
        <circle cx="580" cy="54" r="17" fill="var(--chart-tone)"/>
      </svg>
      <h1 class="headline">
        <span class="headline-emphasis">The Quiet</span>
        <span class="headline-rest">Harbor Surge Unveiled</span>
      </h1>
      <p class="subline">
        <span class="subline-number">7</span>
        <span class="subline-text">Odd Facts Hiding Behind the Quiet Harbor Surge</span>
      </p>
    </section>
  </main>
</body>
</html>
```